Ledgerwise Reach - B2B Demand Generation Website Project

We need a fully functional website for www.ledgerwisereach.example. We are a B2B Demand Generation company, based in London, working with companies such as QRT, VKD, Norvex, Brindlow, Tarvo generating them sales leads for their sales teams. We run this through digital marketing newsletter promotions and have a network of websites. Content syndication, data, demand generation, online marketing. Our logo has just been redone (attached) and we have a holding page already which i would like to use the style / colours. Our logo is bright and vibrant but i dont want the site to be a rainbow. We are expensive, classy, professorial, B2B, intelligent.

Home
About Us
Our Services
Prospora & QA Technology
Intent Data
Testimonials
Contact Us
Updates

Target Market(s)

B2B Marketers (QRT, Velquarion, Tarvo, VKD, Opal Reach, Driftmoor, Harlow Quantis, Technology Companies, Data Companies, Marketing Teams, Tumbleden.

Industry/Entity Type

Marketing

Coding

Coded - Design and coding required

Number of Pages Required

5+ page

Font styles to use
Sans Serif

Requirements
Must have
• Home
About Us
Our Services
Prospora & QA Technology
Intent Data
Testimonials
Contact Us

Simple Pages.

Look classy, intelligent, data experts. I like the video homepages were the image moves at the top. Very soft animation.
Nice to have
• Websites i like:

https://www.vkd.example/
https://www.brevantor.example/
https://www.plumfieldsites.example.co.uk/

Ledgerwise Reach - The Demand Generation Company
Should not have
• Glimpsevault crap images

```html
<!DOCTYPE html>
<html lang="en">
<head>
<meta charset="utf-8">
<title>Ledgerwise Reach – The Demand Generation Company</title>
<link rel="stylesheet" href="https://fonts.googleapis.com/css2?family=Montserrat:wght@300;400;500&family=Poppins:wght@400&display=swap">
<style>
  :root {
    --red: #c0282d;
    --blue: #1f5c99;
    --ink: #111111;
    --muted: #6b6b6b;
    --white: #ffffff;
    --black: #000000;
    --line: #cfcfcf;
  }
  * { box-sizing: border-box; margin: 0; padding: 0; }
  html, body { width: 1200px; height: 2853px; overflow: hidden; }
  body { position: relative; background: var(--white); font-family: "Montserrat", sans-serif; color: var(--ink); }
  .abs { position: absolute; }

  /* hero */
  .hero { position: absolute; left: 0; top: 0; width: 1200px; height: 1187px;
    background: radial-gradient(ellipse at 50% 35%, #ffffff 40%, #efefef 75%, #e2e2e2 100%); }
  .hero-pattern { position: absolute; inset: 0;
    background: linear-gradient(160deg, rgba(200,200,200,.35) 0%, rgba(255,255,255,0) 30%, rgba(255,255,255,0) 70%, rgba(200,200,200,.35) 100%); }
  .menu-toggle { left: 981px; top: 30px; width: 30px; height: 22px; display: flex; flex-direction: column; justify-content: space-between; }
  .menu-toggle span { display: block; height: 4px; background: var(--ink); border-radius: 2px; }
  .brand { left: 0; width: 1200px; top: 128px; text-align: center; }
  .brand-mark { width: 60px; height: 60px; border-radius: 50%; border: 3px solid var(--red); margin: 0 auto 12px; }
  .brand-name { font-size: 40px; font-weight: 400; color: var(--red); line-height: 1; letter-spacing: -0.5px; }
  .brand-tag { font-size: 11px; color: var(--blue); margin-top: 8px; }
  .hero-title { left: 0; width: 1200px; top: 336px; text-align: center; font-family: "Poppins", sans-serif; font-size: 44px; line-height: 42px; font-weight: 400; color: var(--ink); }
  .btn-welcome { left: 547px; top: 525px; width: 106px; height: 36px; border-radius: 18px; background: var(--red); color: var(--white); font-size: 13px; display: flex; align-items: center; justify-content: center; }

  /* about */
  .about-art { left: 208px; top: 789px; width: 213px; height: 211px; border-radius: 8px;
    background: linear-gradient(180deg, #f6e4e4, #f0d3d3); }
  .eyebrow { left: 626px; top: 688px; font-size: 14px; letter-spacing: 4px; color: var(--red); }
  .about-title { left: 643px; top: 722px; font-size: 44px; font-weight: 400; color: var(--blue); }
  .about-text { left: 626px; top: 812px; width: 520px; font-size: 14.5px; line-height: 25.5px; font-weight: 400; color: var(--muted); }
  .btn-outline { left: 627px; top: 1035px; width: 177px; height: 51px; border: 2px solid var(--blue); border-radius: 26px; box-shadow: inset 0 0 0 2px var(--white), inset 0 0 0 3px var(--blue);
    display: flex; align-items: center; justify-content: center; font-size: 14px; letter-spacing: 1px; color: var(--ink); }

  /* services */
  .services { left: 0; top: 1187px; width: 1200px; height: 638px; background: var(--black); }
  .services-title { left: 0; width: 1200px; top: 1268px; text-align: center; font-size: 40px; font-weight: 300; color: var(--white); }
  .service-card { top: 1395px; width: 239px; height: 288px; border: 2px solid var(--white); border-radius: 12px;
    box-shadow: inset 0 0 0 2px var(--black), inset 0 0 0 3px var(--white); }
  .service-icon { position: absolute; left: 78px; top: 20px; width: 82px; height: 82px; border-radius: 8px;
    background: linear-gradient(135deg, #7a1517, #c0282d); }
  .service-name { position: absolute; left: 10px; right: 10px; top: 152px; text-align: center; color: var(--white); font-size: 17px; line-height: 18px; letter-spacing: -0.3px; }
  .service-btn { position: absolute; left: 40px; top: 222px; width: 158px; height: 37px; border: 2px solid var(--white); border-radius: 19px;
    box-shadow: inset 0 0 0 2px var(--black), inset 0 0 0 3px var(--white);
    display: flex; align-items: center; justify-content: center; color: var(--white); font-size: 14px; letter-spacing: 1px; }

  /* stats */
  .stat { top: 2055px; width: 350px; text-align: center; }
  .stat-value { font-size: 62px; font-weight: 300; color: var(--red); line-height: 1; letter-spacing: -2px; }
  .stat-label { font-size: 18px; font-weight: 300; color: var(--blue); margin-top: 14px; }

  /* clients */
  .clients-title { left: 115px; top: 2410px; font-size: 40px; font-weight: 300; color: var(--blue); }
  .client { top: 2400px; height: 52px; display: flex; align-items: center; justify-content: center; gap: 10px; font-size: 30px; font-weight: 500; color: var(--blue); }
  .client-dot { width: 14px; height: 14px; border-radius: 50%; background: var(--blue); }
  .carousel-dots { left: 854px; top: 2502px; display: flex; gap: 11px; }
  .carousel-dots span { width: 5px; height: 5px; border-radius: 50%; background: #d0d0d0; }
  .carousel-dots span.active { background: var(--ink); }

  /* footer */
  .footer { left: 0; top: 2533px; width: 1200px; height: 320px; background: var(--black); }
  .footer-divider { top: 2573px; width: 1px; height: 239px; background: var(--blue); }
  .footer-brand { left: 97px; width: 300px; top: 2596px; text-align: center; }
  .footer-brand .brand-mark { width: 40px; height: 40px; margin-bottom: 10px; }
  .footer-brand .brand-name { font-size: 27px; }
  .footer-brand .brand-tag { font-size: 8px; margin-top: 5px; }
  .footer-address { left: 97px; width: 300px; top: 2724px; text-align: center; color: var(--white); font-size: 15px; line-height: 17px; letter-spacing: 1px; }
  .footer-nav { left: 424px; width: 357px; top: 2605px; list-style: none; text-align: center; }
  .footer-nav li { color: var(--white); font-size: 15px; line-height: 30.8px; letter-spacing: .5px; }
  .social { top: 2651px; width: 12px; height: 12px; border-radius: 50%; background: var(--red); }
  .footer-email { left: 830px; top: 2687px; display: flex; align-items: center; gap: 16px; color: var(--white); font-size: 15px; letter-spacing: 1.5px; }
  .mail-icon { width: 12px; height: 9px; }
  .footer-meta { top: 2826px; font-size: 13px; color: #6a6a6a; }
</style>
</head>
<body>

  <section class="hero">
    <div class="hero-pattern" role="img" aria-label="Soft flowing grey line waves with scattered red particles"></div>
  </section>

  <div class="abs menu-toggle" aria-label="Menu"><span></span><span></span><span></span></div>

  <header class="abs brand">
    <div class="brand-mark"></div>
    <div class="brand-name">ledgerwisereach</div>
    <div class="brand-tag">The Demand Generation Company</div>
  </header>

  <h1 class="abs hero-title">We assist businesses in delivering<br>demand generation strategies</h1>
  <div class="abs btn-welcome">Welcome</div>

  <div class="abs about-art" role="img" aria-label="Line illustration of a group of three people"></div>
  <div class="abs eyebrow">A FEW WORDS</div>
  <svg class="abs" style="left:624px;top:718px" width="270" height="68" viewBox="0 0 270 68" aria-hidden="true">
    <path d="M22 4 C8 10 2 22 4 38 C6 56 22 64 40 64 L232 64 C250 64 262 58 268 44" fill="none" stroke="var(--red)" stroke-width="2.5" stroke-dasharray="1.5 4" stroke-linecap="round"/>
  </svg>
  <h2 class="abs about-title">About Us</h2>
  <p class="abs about-text">Ledgerwise Reach offers multi-channel demand generation services to publishers and technology vendors through our network of lead generation websites and native speaking telemarketing agents. Whether looking for MQL, ABM or BANT campaigns, Ledgerwise Reach can assist you in delivering your demand generation strategy and generate pipeline for your sales teams and/or channel partners.</p>
  <div class="abs btn-outline">READ MORE</div>

  <section class="abs services"></section>
  <svg class="abs" style="left:426px;top:1264px" width="350" height="60" viewBox="0 0 350 60" aria-hidden="true">
    <path d="M2 40 C6 52 14 56 30 56 L308 56 C330 56 344 46 344 30 C344 16 338 8 330 4" fill="none" stroke="var(--red)" stroke-width="2.5" stroke-dasharray="1.5 4" stroke-linecap="round"/>
  </svg>
  <h2 class="abs services-title">Our Services</h2>

  <article class="abs service-card" style="left:222px">
    <div class="service-icon" role="img" aria-label="Icon of a magnifying glass over a chart"></div>
    <h3 class="service-name">Marketing Qualified<br>Leads (MQL)</h3>
    <div class="service-btn">READ MORE</div>
  </article>
  <article class="abs service-card" style="left:481px">
    <div class="service-icon" role="img" aria-label="Icon of a connected group of accounts"></div>
    <h3 class="service-name">Account Based<br>Marketing Leads (ABM)</h3>
    <div class="service-btn">READ MORE</div>
  </article>
  <article class="abs service-card" style="left:740px">
    <div class="service-icon" role="img" aria-label="Icon of a sales person with a rising revenue graph"></div>
    <h3 class="service-name">Sales Qualified Lead /<br>BANT</h3>
    <div class="service-btn">READ MORE</div>
  </article>

  <svg class="abs" style="left:0;top:1990px" width="1200" height="240" viewBox="0 1990 1200 240" aria-hidden="true">
    <g fill="none" stroke="var(--red)" stroke-width="2.5" stroke-dasharray="1.5 4" stroke-linecap="round">
      <path d="M175 2007 C110 2015 74 2060 74 2111 C74 2170 120 2217 180 2217 L318 2217 C385 2217 424 2165 424 2111 C424 2075 428 2045 442 2022"/>
      <path d="M424 2150 C424 2070 466 2007 530 2007 L670 2007 C734 2007 776 2070 776 2150"/>
      <path d="M1025 2007 C1090 2015 1126 2060 1126 2111 C1126 2170 1080 2217 1020 2217 L882 2217 C815 2217 776 2165 776 2111 C776 2075 772 2045 758 2022"/>
    </g>
  </svg>
  <div class="abs stat" style="left:74px"><div class="stat-value">70,000+</div><div class="stat-label">Downloads Per Month</div></div>
  <div class="abs stat" style="left:425px;top:2059px"><div class="stat-value">25,000+</div><div class="stat-label">Leads Delivered Per Month</div></div>
  <div class="abs stat" style="left:776px"><div class="stat-value">50+</div><div class="stat-label">Countries We Can Reach</div></div>

  <h2 class="abs clients-title">Who We Work With</h2>
  <div class="abs client" style="left:618px;width:160px"><span class="client-dot"></span>Tarvo</div>
  <div class="abs client" style="left:800px;width:170px">Corvane</div>
  <div class="abs client" style="left:985px;width:180px">VKD</div>
  <div class="abs carousel-dots"><span></span><span></span><span></span><span class="active"></span></div>

  <footer class="abs footer"></footer>
  <div class="abs footer-divider" style="left:424px"></div>
  <div class="abs footer-divider" style="left:781px"></div>

  <div class="abs footer-brand">
    <div class="brand-mark"></div>
    <div class="brand-name">ledgerwisereach</div>
    <div class="brand-tag">The Demand Generation Company</div>
  </div>
  <address class="abs footer-address" style="font-style:normal">14 Arbour Lane<br>London<br>England</address>

  <ul class="abs footer-nav">
    <li>Home</li>
    <li>About Us</li>
    <li>Our Services</li>
    <li>Prospora &amp; QA Technology</li>
    <li>Intent Data</li>
    <li>Contact Us</li>
  </ul>

  <span class="abs social" style="left:900px" aria-label="Social profile"></span>
  <span class="abs social" style="left:952px" aria-label="Social profile"></span>
  <span class="abs social" style="left:1004px" aria-label="Social profile"></span>

  <div class="abs footer-email">
    <svg class="mail-icon" viewBox="0 0 12 9" aria-hidden="true"><rect width="12" height="9" rx="1" fill="var(--red)"/><path d="M0.5 1 L6 5 L11.5 1" fill="none" stroke="var(--black)" stroke-width="1"/></svg>
    <span>info@ledgerwisereach.example</span>
  </div>

  <div class="abs footer-meta" style="left:147px">Copyright © 2020 Ledgerwise Reach</div>
  <div class="abs footer-meta" style="left:879px">website by Quillmark Studio</div>

</body>
</html>
```